'Bright Ledger Hidden Keys' Book Cover

I need a professional book cover design for my new upcoming book that shows people how to get a high credit score.

Here are my two websites:

https://www.moneywordbank-lexa.info
https://moneywordbank-lexa.com/

I am looking for a clean, professional design that pops (emotional touch) and separates from the other books that are on the market. Cover aspect ratio 1:4 for Pagewisp version and 1:5 for the paperback version. Yellow or blue are good colors - but not must. See the basic examples that I provided. File delivery format PDF.

Book Title: Bright Ledger Hidden Keys
Byline: The Quick Lift And Mend Manual for Stellar Borrowing

Currently on Brindlecart pre-order:
https://www.brindlecart.example/Bright-Ledger-Hidden-Keys-Stellar-ebook/dp/Q48MPLRT71

I am the author of 36 published books on Brindlecart. My author profile is here:
brindlecart.example/author/gideonvarly

Targeted audience: People that want to improve or repair their bad credit score.

Target Market(s)

People/consumers in the US that want to improve or repair their credit score.

Industry/Entity Type

Consumer

Font styles to use
Sans Serif

Colors

Designer to choose colors to be used in the design.

Requirements
Must have
• Author name, Title, byline, and graphic element(s).
Nice to have
• - 2020 edition logo / batch

```html
<!DOCTYPE html>
<html lang="en">
<head>
<meta charset="utf-8">
<title>Bright Ledger Hidden Keys — Book Cover</title>
<link href="https://fonts.googleapis.com/css2?family=Montserrat:wght@300;700;800;900&display=swap" rel="stylesheet">
<style>
  :root {
    --purple-deep: #64308f;
    --purple-glow: #8f409a;
    --yellow-core: #fbee1d;
    --yellow-mid: #efd24a;
    --yellow-edge: #dba312;
    --tan: #c9956a;
    --tan-soft: #b38578;
    --ink: #3a3a3c;
    --card-blue: #2e5fa0;
    --card-blue-light: #3a6db0;
    --card-edge: #244f88;
  }
  html, body {
    margin: 0;
    padding: 0;
    width: 849px;
    height: 1200px;
    overflow: hidden;
    background: #ffffff;
  }
  .cover {
    position: relative;
    width: 849px;
    height: 1200px;
    overflow: hidden;
    font-family: 'Montserrat', sans-serif;
    color: var(--ink);
  }
  .cover__backdrop {
    position: absolute;
    inset: 0;
    width: 849px;
    height: 1200px;
  }
  .cover__title {
    position: absolute;
    left: 0;
    width: 849px;
    text-align: center;
    margin: 0;
    line-height: 1;
    white-space: nowrap;
  }
  .title-lead {
    top: 488px;
    font-weight: 900;
    font-size: 176px;
    letter-spacing: -2px;
  }
  .title-middle {
    top: 688px;
    font-weight: 300;
    font-size: 82px;
    letter-spacing: 0;
  }
  .title-tail {
    top: 782px;
    font-weight: 800;
    font-size: 158px;
    letter-spacing: 18px;
    text-indent: 18px;
  }
  .cover__byline {
    position: absolute;
    left: 0;
    top: 1018px;
    width: 849px;
    text-align: center;
    margin: 0;
    font-weight: 700;
    font-size: 31px;
    line-height: 38px;
    letter-spacing: 0.3px;
    text-transform: uppercase;
  }
  .cover__author {
    position: absolute;
    left: 0;
    top: 1128px;
    width: 849px;
    text-align: center;
    margin: 0;
    font-weight: 700;
    font-size: 22px;
    line-height: 1;
    letter-spacing: 4px;
    text-transform: uppercase;
  }
</style>
</head>
<body>
<main class="cover">
  <svg class="cover__backdrop" viewBox="0 0 849 1200" xmlns="http://www.w3.org/2000/svg">
    <defs>
      <radialGradient id="sky" cx="0.45" cy="0.3" r="0.7">
        <stop offset="0" stop-color="var(--purple-glow)"/>
        <stop offset="1" stop-color="var(--purple-deep)"/>
      </radialGradient>
      <radialGradient id="sand" cx="390" cy="793" r="560" gradientUnits="userSpaceOnUse">
        <stop offset="0" stop-color="var(--yellow-core)"/>
        <stop offset="0.45" stop-color="var(--yellow-mid)"/>
        <stop offset="1" stop-color="var(--yellow-edge)"/>
      </radialGradient>
      <linearGradient id="card-fill" x1="0" y1="0" x2="1" y2="1">
        <stop offset="0" stop-color="var(--card-blue-light)"/>
        <stop offset="1" stop-color="var(--card-blue)"/>
      </linearGradient>
    </defs>
    <rect class="sky" width="849" height="1200" fill="url(#sky)"/>
    <path class="wave-back" fill="var(--tan-soft)" d="M0,322 C60,345 110,352 160,382 C210,410 250,432 300,412 C350,392 380,360 430,352 C470,346 470,345 480,340 C520,320 560,350 600,360 C630,370 620,420 640,450 C670,480 700,500 730,520 C780,560 820,590 849,610 L849,1200 L0,1200 Z"/>
    <path class="wave-sand" fill="url(#sand)" d="M0,378 C40,372 80,370 120,388 C170,410 210,440 260,420 C310,400 360,405 400,408 C440,412 460,380 490,362 C520,345 560,375 600,385 C625,392 640,450 670,490 C700,530 715,560 745,580 C780,600 820,625 849,640 L849,1200 L0,1200 Z"/>
    <g class="card-art" role="img" aria-label="Illustration of a blue bank card with chip, number and holder name, tilted over the horizon">
      <rect x="457" y="150" width="310" height="190" rx="12" fill="url(#card-fill)" stroke="var(--card-edge)" stroke-width="2" transform="rotate(-37 612 245)"/>
    </g>
  </svg>

  <h1 class="cover__title title-lead">BRIGHT</h1>
  <p class="cover__title title-middle">LEDGER HIDDEN</p>
  <p class="cover__title title-tail">KEYS</p>

  <p class="cover__byline">The Quick Lift And Mend Manual<br>for Stellar Borrowing</p>
  <p class="cover__author">Gideon Varly</p>
</main>
</body>
</html>
```